Real Estate Company / Capital Needs Cards!

need business cards designed using the logos that were just designed by sketchhive.

Reason: per designers request deadline extended 1 day…thank you.

Target Market(s)

Investors and clients looking to purchase real estate or invest in the business.

Industry/Entity Type

Business

Requirements
Must have
• two designs - one for the real estate logo and one for the capital logo, similar but slightly different.
Nice to have
• something to make it pop (perhaps on the back)
Should not have
• much color

```html
<!DOCTYPE html>
<html lang="en">
<head>
<meta charset="utf-8">
<title>Velmora Real Estate — Business Cards</title>
<link rel="stylesheet" href="https://fonts.googleapis.com/css2?family=Cinzel:wght@400&family=Roboto:wght@300;400&display=swap">
<style>
  :root {
    --backdrop: #2b2a2a;
    --card-black: #141414;
    --card-white: #f3f3f1;
    --brand-grey: #b9b9bb;
    --ink: #3a3a3a;
    --ink-soft: #7a7a7a;
    --bar-grey: #a9a9ab;
    --bar-text: #f4f4f4;
    --bar-label: #e0e0e0;
  }
  * { margin: 0; padding: 0; box-sizing: border-box; }
  html, body {
    width: 1200px; height: 800px; overflow: hidden;
    background: var(--backdrop);
  }
  .sheet {
    width: 1200px; height: 800px;
    display: flex; align-items: center; justify-content: center; gap: 60px;
  }
  .card {
    width: 525px; height: 300px;
    border-radius: 4px;
    position: relative; overflow: hidden;
    box-shadow: 0 14px 30px rgba(0,0,0,.45);
  }
  /* Front */
  .card--front {
    background: var(--card-black);
    display: flex; align-items: center; justify-content: center;
  }
  .brand {
    display: flex; align-items: center; gap: 14px;
    color: var(--brand-grey);
    font-family: "Cinzel", serif; font-weight: 400;
  }
  .brand__square {
    width: 46px; height: 46px; background: var(--brand-grey);
  }
  .brand__name { display: flex; flex-direction: column; line-height: 1; }
  .brand__title { font-size: 34px; letter-spacing: 1px; }
  .brand__sub { font-size: 13px; letter-spacing: 3.2px; margin-top: 4px; }
  /* Back */
  .card--back { background: var(--card-white); }
  .holder {
    position: absolute; left: 70px; top: 52px;
    font-family: "Roboto", sans-serif; text-align: right;
  }
  .holder__name { font-size: 24px; font-weight: 400; color: var(--ink); }
  .holder__role { font-size: 12px; font-weight: 300; color: var(--ink-soft); letter-spacing: 1px; }
  .contacts { position: absolute; left: 0; right: 0; top: 120px; list-style: none; }
  .contact {
    display: flex; align-items: center; gap: 12px;
    height: 22px; margin-bottom: 12px;
    background: var(--bar-grey);
    border-radius: 11px 0 0 11px;
    padding-left: 16px;
    font-family: "Roboto", sans-serif; font-size: 11px;
  }
  .contact:nth-child(1) { margin-left: 50px; }
  .contact:nth-child(2) { margin-left: 95px; }
  .contact:nth-child(3) { margin-left: 140px; }
  .contact:nth-child(4) { margin-left: 185px; }
  .contact:nth-child(5) { margin-left: 230px; }
  .contact__label { color: var(--bar-label); font-weight: 300; width: 46px; text-align: right; }
  .contact__value { color: var(--bar-text); font-weight: 400; }
</style>
</head>
<body>
  <main class="sheet">
    <section class="card card--back" aria-label="Card back">
      <div class="holder">
        <p class="holder__name">Adrian Vale</p>
        <p class="holder__role">C.E.O.</p>
      </div>
      <ul class="contacts">
        <li class="contact"><span class="contact__label">address</span><span class="contact__value">Harbor Lane 48, 2210 Westfield</span></li>
        <li class="contact"><span class="contact__label">phone</span><span class="contact__value">+0144 280 613</span></li>
        <li class="contact"><span class="contact__label">mobile</span><span class="contact__value">+0144 280 927</span></li>
        <li class="contact"><span class="contact__label">email</span><span class="contact__value">hello@velmora.net</span></li>
        <li class="contact"><span class="contact__label">web</span><span class="contact__value">www.velmora.com</span></li>
      </ul>
    </section>
    <section class="card card--front" aria-label="Card front">
      <div class="brand">
        <span class="brand__square" aria-hidden="true"></span>
        <span class="brand__name">
          <span class="brand__title">VELMORA</span>
          <span class="brand__sub">REAL ESTATE</span>
        </span>
      </div>
    </section>
  </main>
</body>
</html>
```